Diagram of Marrowfen’s history for website

This project is to design the attached diagram along the lines of the attached image but in our branding - style guide attached. The diagram will be going on the Marrowfen website - www.marrowfen.au.

```html
<!DOCTYPE html>
<html lang="en">
<head>
<meta charset="utf-8">
<title>Marrowfen History Timeline</title>
<link href="https://fonts.googleapis.com/css2?family=Open+Sans:wght@400;600;700&display=swap" rel="stylesheet">
<style>
  :root {
    --c2017: #d4a88e;
    --c2018: #9d7463;
    --c2019: #6ba57f;
    --c2021: #5f8b6b;
    --c2022: #7b9fa6;
    --c2023: #49676a;
    --axis: #7e8386;
    --ink: #3d3d3d;
    --ink-strong: #1f1f1f;
    --bg: #fdfdfd;
  }
  * { margin: 0; padding: 0; box-sizing: border-box; }
  html, body { width: 1200px; height: 949px; overflow: hidden; background: var(--bg); }
  .timeline {
    position: relative; width: 1200px; height: 949px;
    font-family: "Open Sans", sans-serif; color: var(--ink);
  }
  .timeline-art { position: absolute; inset: 0; }
  .year {
    position: absolute; font-size: 56px; font-weight: 700;
    line-height: 1; letter-spacing: -1.5px;
  }
  .event { position: absolute; }
  .event-title {
    font-size: 18px; font-weight: 700; line-height: 20px;
    letter-spacing: -0.1px; text-transform: uppercase;
  }
  .event-text { font-size: 15px; line-height: 20px; margin-top: 2px; }
  .event-text strong { color: var(--ink-strong); font-weight: 700; }
  .tight .event-text { line-height: 18px; }
  .y2017 { color: var(--c2017); }
  .y2018 { color: var(--c2018); }
  .y2019 { color: var(--c2019); }
  .y2021 { color: var(--c2021); }
  .y2022 { color: var(--c2022); }
  .y2023 { color: var(--c2023); }
</style>
</head>
<body>
<main class="timeline">
  <svg class="timeline-art" width="1200" height="949" viewBox="0 0 1200 949" aria-hidden="true">
    <!-- axis -->
    <g stroke="var(--axis)" stroke-width="14" fill="none">
      <line x1="134" y1="486" x2="233" y2="486"/>
      <line x1="266" y1="486" x2="364" y2="486"/>
      <line x1="397" y1="486" x2="495" y2="486"/>
      <line x1="528" y1="486" x2="626" y2="486"/>
      <line x1="659" y1="486" x2="781" y2="486"/>
      <line x1="814" y1="486" x2="1062" y2="486"/>
      <polyline points="1061,450 1098,486 1061,520" stroke-linecap="round" stroke-linejoin="round" stroke-width="16"/>
    </g>
    <!-- stems -->
    <g stroke-width="8">
      <line x1="117" y1="504" x2="117" y2="828" stroke="var(--c2017)"/>
      <line x1="249" y1="286" x2="249" y2="467" stroke="var(--c2018)"/>
      <line x1="380" y1="504" x2="380" y2="647" stroke="var(--c2019)"/>
      <line x1="511" y1="286" x2="511" y2="467" stroke="var(--c2021)"/>
      <line x1="642" y1="504" x2="642" y2="856" stroke="var(--c2022)"/>
      <line x1="797" y1="77" x2="797" y2="467" stroke="var(--c2023)"/>
    </g>
    <!-- axis nodes -->
    <g>
      <circle cx="117" cy="486" r="12.5" fill="var(--c2017)"/><circle cx="117" cy="486" r="9.5" fill="#fff"/><circle cx="117" cy="486" r="6.5" fill="var(--c2017)"/>
      <circle cx="249" cy="486" r="12.5" fill="var(--c2018)"/><circle cx="249" cy="486" r="9.5" fill="#fff"/><circle cx="249" cy="486" r="6.5" fill="var(--c2018)"/>
      <circle cx="380" cy="486" r="12.5" fill="var(--c2019)"/><circle cx="380" cy="486" r="9.5" fill="#fff"/><circle cx="380" cy="486" r="6.5" fill="var(--c2019)"/>
      <circle cx="511" cy="486" r="12.5" fill="var(--c2021)"/><circle cx="511" cy="486" r="9.5" fill="#fff"/><circle cx="511" cy="486" r="6.5" fill="var(--c2021)"/>
      <circle cx="642" cy="486" r="12.5" fill="var(--c2022)"/><circle cx="642" cy="486" r="9.5" fill="#fff"/><circle cx="642" cy="486" r="6.5" fill="var(--c2022)"/>
      <circle cx="797" cy="486" r="12.5" fill="var(--c2023)"/><circle cx="797" cy="486" r="9.5" fill="#fff"/><circle cx="797" cy="486" r="6.5" fill="var(--c2023)"/>
      <circle cx="1077" cy="486" r="12.5" fill="var(--axis)"/><circle cx="1077" cy="486" r="9.5" fill="#fff"/><circle cx="1077" cy="486" r="6.5" fill="var(--axis)"/>
    </g>
    <!-- event dots -->
    <g>
      <g fill="var(--c2017)"><circle cx="117" cy="593" r="10"/><circle cx="117" cy="781" r="10"/><circle cx="117" cy="827" r="10"/></g>
      <g fill="var(--c2018)"><circle cx="249" cy="286" r="10"/></g>
      <g fill="var(--c2019)"><circle cx="380" cy="584" r="10"/><circle cx="380" cy="647" r="10"/></g>
      <g fill="var(--c2021)"><circle cx="511" cy="286" r="10"/></g>
      <g fill="var(--c2022)"><circle cx="642" cy="584" r="10"/><circle cx="642" cy="678" r="10"/><circle cx="642" cy="772" r="10"/><circle cx="642" cy="856" r="10"/></g>
      <g fill="var(--c2023)"><circle cx="797" cy="77" r="10"/><circle cx="797" cy="136" r="10"/><circle cx="797" cy="217" r="10"/><circle cx="797" cy="279" r="10"/><circle cx="797" cy="346" r="10"/></g>
    </g>
  </svg>

  <!-- 2017 -->
  <div class="year y2017" style="left:138px;top:514px;">2017</div>
  <div class="event y2017" style="left:142px;top:575px;">
    <h3 class="event-title">Marrowfen<br>Commences</h3>
    <p class="event-text"><strong>Maren</strong> Started the<br>business with 25 years’<br>Experience working for<br>Government Disability<br>&amp; community Services.<br>Our First office is in<br><strong>Brantley</strong></p>
  </div>
  <div class="event y2017" style="left:142px;top:769px;">
    <h3 class="event-title">NCSS Provider</h3>
    <p class="event-text"><strong>Marrowfen</strong> becomes a NCSS<br>Registered Provider</p>
  </div>

  <!-- 2018 -->
  <div class="event y2018 tight" style="left:269px;top:276px;">
    <h3 class="event-title">Civic-Corporation</h3>
    <p class="event-text">Clinic Expansion<br>Marrowfen moves offices<br>twice in Brantley due to<br>Growth &amp; Expansion.<br>Clinic Established</p>
  </div>
  <div class="year y2018" style="left:269px;top:416px;">2018</div>

  <!-- 2019 -->
  <div class="year y2019" style="left:401px;top:514px;">2019</div>
  <div class="event y2019" style="left:405px;top:575px;">
    <h3 class="event-title">Move to Ellerby</h3>
    <p class="event-text"><strong>Marrowfen</strong> moves to<br>Ellerby due to further<br>Growth &amp; Expansion</p>
  </div>

  <!-- 2021 -->
  <div class="event y2021 tight" style="left:533px;top:276px;">
    <h3 class="event-title">Civic-Corporation</h3>
    <p class="event-text"><strong>Marrowfen</strong> becomes a<br>accredited Civic-Corporation<br>having met the highest<br>standards of environmental,<br>society &amp; Community<br>performance</p>
  </div>
  <div class="year y2021" style="left:533px;top:416px;">2021</div>

  <!-- 2022 -->
  <div class="year y2022" style="left:660px;top:514px;">2022</div>
  <div class="event y2022" style="left:667px;top:575px;">
    <h3 class="event-title">Corvane Best of Business</h3>
    <p class="event-text"><strong>Marrowfen</strong> wins the Corvane<br>Best of Business Award (Vic)<br>for Building Communities</p>
  </div>
  <div class="event y2022" style="left:667px;top:669px;">
    <h3 class="event-title">Move to Dunmore</h3>
    <p class="event-text"><strong>Marrowfen</strong> moves to a<br>larger premises<br>in <strong>dunmore</strong></p>
  </div>
  <div class="event y2022" style="left:667px;top:763px;">
    <h3 class="event-title">Partnerships</h3>
    <p class="event-text">Partnership establised with<br><strong>Tarawind School</strong> for Children with<br>Disability &amp; <strong>Yarrin Kora<br>(Eastvale University)</strong></p>
  </div>

  <!-- 2023 -->
  <div class="event y2023 tight" style="left:822px;top:66px;">
    <h3 class="event-title">Rebranding</h3>
    <p class="event-text">Marrowfen Rebranded</p>
  </div>
  <div class="event y2023" style="left:822px;top:114px;">
    <h3 class="event-title">Reconciliation<br>Action Plan (RAP)</h3>
    <p class="event-text"><strong>Marrowfen's</strong> Reflect RAP<br>Developed &amp; Endorsed</p>
  </div>
  <div class="event y2023 tight" style="left:821px;top:206px;">
    <h3 class="event-title">Client Advisory Group</h3>
    <p class="event-text">Marrowfen's Client Advisory<br>Group Commences</p>
  </div>
  <div class="event y2023 tight" style="left:821px;top:270px;">
    <h3 class="event-title">E-Learning Platform</h3>
    <p class="event-text">Marrowfen E-Learning<br>Platform launched</p>
  </div>
  <div class="event y2023 tight" style="left:821px;top:336px;">
    <h3 class="event-title">Prism Tick</h3>
    <p class="event-text"><strong>Marrowfen</strong> Achieves<br>Prism Tick<br>Accreditation</p>
  </div>
  <div class="year y2023" style="left:820px;top:416px;">2023</div>
</main>
</body>
</html>
```